New Business Card for our Indoor Golf Training Facility

We are looking for designs for a new business card for our indoor golf training facility. Attached is our logo, our logo with our slogan, and here is our elevator pitch (What makes us different from the others) not sure if all the info will fit on one card, maybe you can condense the elevator pitch? here is the info

Elevator Pitch
We work with serious golfers and those that want to be serious golfers…
to make you better, faster, at all phases of the game…
We use the same state-of-the-art technology as professional golfers…
which produces data sets that shows your improvement in real time.
Our facility is available 24/7 to our members, which allows you to improve on your time.

our website: www.brambleteegolf.com

Target Market(s)

Golfers

Font styles to use
Serif
Sans Serif

Colors
ec1f27
f59195
fbd4d5
919191
d3d3d3
1b1b1b

Requirements
Must have
• our logo or our logo with the slogan, elevator pitch (can be condensed or shortened)

```html
<!DOCTYPE html>
<html lang="en">
<head>
<meta charset="utf-8">
<title>Bramble Tee Golf – Business Card</title>
<link href="https://fonts.googleapis.com/css2?family=Open+Sans:wght@400;600;700;800&display=swap" rel="stylesheet">
<style>
  :root {
    --red: #ec1f27;
    --red-soft: #ef4138;
    --black: #1b1b1b;
    --ink: #111111;
    --white: #ffffff;
    --stage: #d3d3d3;
  }
  * { margin: 0; padding: 0; box-sizing: border-box; }
  html, body { width: 1200px; height: 782px; overflow: hidden; }
  body {
    background: var(--stage);
    font-family: "Open Sans", Arial, sans-serif;
    display: flex;
    flex-direction: column;
    align-items: center;
    justify-content: center;
    gap: 40px;
  }
  .card {
    position: relative;
    width: 560px;
    height: 320px;
    overflow: hidden;
    box-shadow: 0 6px 18px rgba(0,0,0,.25);
  }
  .card__art { position: absolute; inset: 0; }

  /* Pitch side */
  .card--pitch { background: var(--red-soft); color: var(--white); }
  .pitch {
    position: absolute;
    left: 34px; top: 30px;
    width: 360px;
    font-size: 13.5px;
    line-height: 1.3;
  }
  .pitch__title { font-weight: 700; font-size: 15px; letter-spacing: .3px; margin-bottom: 4px; }
  .pitch p { margin-bottom: 3px; }
  .pitch__visit { margin-top: 6px; white-space: nowrap; }
  .pitch__url { font-weight: 800; font-size: 16px; }

  /* Contact side */
  .card--contact { background: var(--ink); color: var(--white); }
  .contact {
    position: absolute;
    right: 34px; top: 108px;
    text-align: right;
  }
  .brand__name { color: var(--red); font-weight: 800; font-size: 24px; line-height: 1; }
  .brand__slogan { color: var(--red); font-size: 9.5px; margin-top: 4px; }
  .person { margin-top: 18px; }
  .person__name { color: var(--red); font-weight: 600; font-size: 19px; line-height: 1.15; }
  .person__role { font-size: 15px; line-height: 1.2; }
  .details { margin-top: 8px; font-size: 14.5px; line-height: 1.3; }
  .details__row { display: flex; align-items: center; justify-content: flex-end; gap: 6px; }
  .icon { width: 12px; height: 12px; flex: none; }
</style>
</head>
<body>

  <section class="card card--pitch">
    <svg class="card__art" viewBox="0 0 560 320" aria-hidden="true">
      <circle cx="478" cy="196" r="122" fill="var(--white)" stroke="var(--red-soft)" stroke-width="16"/>
    </svg>
    <div class="pitch">
      <h2 class="pitch__title">ELEVATOR PITCH</h2>
      <p>We work with serious golfers and those<br>that want to be serious golfers…<br>to make you better, faster, at all<br>phases of the game…</p>
      <p>We use the same state-of-the-art<br>technology as professional golfers…<br>which produces data sets that shows<br>your improvement in real time.</p>
      <p>Our facility is available 24/7 to our<br>members, which allows<br>you to improve on your time.</p>
      <p class="pitch__visit">Visit <span class="pitch__url">www.brambleteegolf.com</span> for more details.</p>
    </div>
  </section>

  <section class="card card--contact">
    <svg class="card__art" viewBox="0 0 560 320" aria-hidden="true">
      <circle cx="88" cy="78" r="150" fill="var(--white)" stroke="var(--red-soft)" stroke-width="26"/>
    </svg>
    <div class="contact">
      <div class="brand__name">Bramble Tee Golf</div>
      <div class="brand__slogan">Train Smart. Play Sharp. Go Lower.</div>
      <div class="person">
        <div class="person__name">Daniel Hart</div>
        <div class="person__role">Managing Director</div>
      </div>
      <div class="details">
        <div class="details__row">555-014-2290
          <svg class="icon" viewBox="0 0 12 12"><circle cx="6" cy="6" r="6" fill="var(--red)"/><path d="M4 3.2l1 1.3-.6.7a3.6 3.6 0 0 0 1.9 1.9l.7-.6 1.3 1-.7 1.2C5.8 8.4 3.6 6.2 3.3 3.9z" fill="var(--white)"/></svg>
        </div>
        <div class="details__row">www.brambleteegolf.com
          <svg class="icon" viewBox="0 0 12 12"><circle cx="6" cy="6" r="6" fill="var(--red)"/><circle cx="6" cy="6" r="3" fill="none" stroke="var(--white)" stroke-width="1"/><path d="M3 6h6M6 3v6" stroke="var(--white)" stroke-width=".8"/></svg>
        </div>
        <div class="details__row">1480 W. Orchard Ln. Unit B4</div>
        <div class="details__row">Fairmont, OH 45000</div>
      </div>
    </div>
  </section>

</body>
</html>
```